"Kolvarisk" Show on Strovana and plavento needs a thumbnail.

Hello, I need a thumbnail image for a new show I want to start Strovana and Plavento soon. This show represents different styles of music out of all EDM genres mixed to approx. one hour sets. Please find attached CD covers I really like in their style and which can be used as inspiration. This show should be released on a weekly basis. So I want to attach my logo which needs to be thumbnailed / image as well

Target Market(s)

Young EDM Lovers

Industry/Entity Type

Plavento

Requirements
Must have
• The cover needs to have the above mentioned title in a cool lettering and the name of the artist (which can be found in the attached pictures in color and style. should represent electronic music.
Nice to have
• I imagine child of earth ball instead of speakers or symbols in the cover. It shall represent the (re-) union which happens when young people come together and share their passion for music. Does not matter which style it is. It's also nice to have a space for adding social media information on the thumbnail.
Should not have
• Should not be too colorful. No comic style.

```html
<!DOCTYPE html>
<html lang="en">
<head>
<meta charset="utf-8">
<title>Kolvarisk – Show Thumbnail</title>
<link rel="stylesheet" href="https://fonts.googleapis.com/css2?family=Archivo+Black&display=swap">
<style>
  :root {
    --yellow: #d9cc1c;
    --yellow-dark: #8c8420;
    --speaker: #2f3e57;
    --speaker-deep: #1d2638;
    --brand-blue: #2673b8;
    --brand-cream: #f1ecd8;
    --band-black: #050505;
    --gold-light: #e9b93e;
    --ink-dark: #1e1a10;
    --globe-blue: #2d78c4;
    --globe-gold: #e3b35e;
  }
  * { margin: 0; padding: 0; box-sizing: border-box; }
  html, body { width: 729px; height: 1200px; overflow: hidden; background: #fff; }
  .thumbnail { position: relative; width: 729px; height: 1200px; font-family: "Archivo Black", "Arial Black", sans-serif; }

  .panel { position: absolute; left: 0; width: 729px; overflow: hidden; }
  .panel--top { top: 0; height: 600px; }
  .panel--bottom { top: 604px; height: 596px; }

  .speaker-photo {
    position: absolute; inset: 0;
    background:
      radial-gradient(ellipse 62% 52% at 38% 52%, var(--speaker) 0%, var(--speaker) 70%, var(--speaker-deep) 86%, transparent 88%),
      linear-gradient(135deg, var(--yellow) 0%, #c8bb1d 55%, var(--yellow-dark) 100%);
  }
  .panel--top .speaker-photo {
    background:
      radial-gradient(ellipse 66% 62% at 30% 56%, var(--speaker) 0%, #3b4b66 55%, var(--speaker-deep) 86%, transparent 88%),
      linear-gradient(135deg, var(--yellow) 0%, #c8bb1d 55%, var(--yellow-dark) 100%);
  }

  .globe {
    position: absolute; border-radius: 50%;
    background: radial-gradient(circle at 45% 40%, #8ec3ee 0%, var(--globe-blue) 45%, var(--globe-gold) 78%, #b5812e 100%);
    box-shadow: 0 6px 14px rgba(0,0,0,.45);
  }
  .panel--top .globe { left: 130px; top: 246px; width: 208px; height: 150px; }
  .panel--bottom .globe { left: 133px; top: 246px; width: 216px; height: 156px; }

  .rank {
    position: absolute; line-height: 1; letter-spacing: -3px; font-size: 86px;
    text-shadow: 2px 3px 4px rgba(0,0,0,.55); white-space: nowrap;
  }
  .rank .rank-num { font-size: 1.38em; }
  .rank--gold { left: 32px; top: 400px; color: var(--gold-light); }
  .rank--dark { right: 21px; top: 0; color: var(--ink-dark); }

  .brand-band { position: absolute; display: flex; align-items: center; justify-content: center; }
  .brand-band--top { top: 0; left: 0; width: 729px; height: 128px; }
  .brand-band--bottom { top: 413px; left: 8px; width: 716px; height: 139px; background: var(--band-black); }
  .brand-rule { position: absolute; height: 9px; background: var(--brand-blue); }
  .brand-band--top .brand-rule { left: 6px; right: 6px; }
  .brand-band--top .brand-rule--upper { top: 0; }
  .brand-band--top .brand-rule--lower { top: 116px; }
  .brand-band--bottom .brand-rule { left: 14px; right: 14px; }
  .brand-band--bottom .brand-rule--upper { top: 17px; }
  .brand-band--bottom .brand-rule--lower { top: 109px; }

  .brand-name { line-height: 1; white-space: nowrap; }
  .brand-band--top .brand-name { font-size: 100px; letter-spacing: 9px; color: var(--brand-blue); }
  .brand-band--bottom .brand-name { font-size: 74px; letter-spacing: 10px; color: var(--brand-cream); }
</style>
</head>
<body>
<main class="thumbnail">
  <section class="panel panel--top">
    <div class="speaker-photo" role="img" aria-label="Close-up photo of a dark loudspeaker cone on a grungy yellow background"></div>
    <div class="globe" role="img" aria-label="Glossy globe showing the Atlantic with gold continents, set in the speaker centre"></div>
    <div class="brand-band brand-band--top">
      <span class="brand-rule brand-rule--upper"></span>
      <span class="brand-name">KOLVARISK</span>
      <span class="brand-rule brand-rule--lower"></span>
    </div>
    <p class="rank rank--gold">No.<span class="rank-num">1</span></p>
  </section>

  <section class="panel panel--bottom">
    <div class="speaker-photo" role="img" aria-label="Close-up photo of a dark loudspeaker cone on a grungy yellow background"></div>
    <div class="globe" role="img" aria-label="Glossy globe showing the Atlantic with gold continents, set in the speaker centre"></div>
    <p class="rank rank--dark">No.<span class="rank-num">1</span></p>
    <div class="brand-band brand-band--bottom">
      <span class="brand-rule brand-rule--upper"></span>
      <span class="brand-name">KOLVARISK</span>
      <span class="brand-rule brand-rule--lower"></span>
    </div>
  </section>
</main>
</body>
</html>
```